Pinecrest Lockworks Business Card Design

Double Sided Business Card Design for a Locksmith company specializing in Safecracking, safe & vault service.

```html
<!DOCTYPE html>
<html lang="en">
<head>
<meta charset="utf-8">
<title>Pinecrest Lockworks Business Card</title>
<link href="https://fonts.googleapis.com/css2?family=Roboto:wght@400;500;700&display=swap" rel="stylesheet">
<style>
  :root {
    --bg: #d3d6d7;
    --paper: #eeeeea;
    --ink: #1d1d1d;
    --green: #1d6b2c;
    --black: #0d0d0d;
    --light: #e2e2e2;
    --rule: #555;
  }
  * { margin: 0; padding: 0; box-sizing: border-box; }
  html, body { width: 1200px; height: 1051px; overflow: hidden; }
  body {
    background: var(--bg);
    font-family: 'Roboto', Arial, sans-serif;
    display: flex;
    flex-direction: column;
    align-items: center;
    justify-content: center;
    gap: 60px;
  }
  .card {
    width: 640px;
    height: 366px;
    position: relative;
    box-shadow: 0 10px 24px rgba(0,0,0,0.18);
  }
  .card--front { background: var(--paper); border-bottom: 3px solid var(--green); }
  .card--back { background: var(--black); display: flex; align-items: center; justify-content: center; }

  .brand { display: flex; align-items: center; gap: 14px; }
  .brand__mark { width: 34px; height: 34px; border-radius: 50%; background: var(--green); flex: none; }
  .brand__name { font-weight: 700; color: var(--green); text-transform: uppercase; line-height: 1; letter-spacing: 0.5px; }

  .card--front .brand { position: absolute; left: 44px; top: 112px; width: 250px; }
  .card--front .brand__name { font-size: 24px; }

  .divider { position: absolute; left: 318px; top: 92px; width: 1px; height: 120px; background: var(--rule); }

  .contact { position: absolute; left: 340px; top: 92px; }
  .contact__name { font-size: 17px; font-weight: 700; color: var(--green); letter-spacing: 0.4px; }
  .contact__title { font-size: 15px; font-weight: 500; color: var(--ink); margin-bottom: 8px; }
  .contact__list { list-style: none; }
  .contact__item { display: flex; align-items: center; gap: 8px; font-size: 14.5px; color: var(--ink); line-height: 1.45; }
  .icon { width: 12px; height: 12px; fill: var(--green); flex: none; }

  .address { position: absolute; left: 44px; top: 258px; display: flex; align-items: center; gap: 8px; font-size: 15px; color: var(--ink); }
  .address .icon { width: 12px; height: 16px; }

  .card--back .brand__mark { width: 64px; height: 64px; }
  .card--back .brand__name { font-size: 40px; }
</style>
</head>
<body>
  <section class="card card--front">
    <div class="brand">
      <span class="brand__mark"></span>
      <span class="brand__name">Pinecrest Lockworks</span>
    </div>
    <div class="divider"></div>
    <div class="contact">
      <p class="contact__name">MARTIN KESSLER</p>
      <p class="contact__title">Managing Director</p>
      <ul class="contact__list">
        <li class="contact__item"><svg class="icon" viewBox="0 0 24 24"><path d="M6.6 10.8a15 15 0 006.6 6.6l2.2-2.2a1 1 0 011-.25 11.4 11.4 0 003.6.57 1 1 0 011 1V20a1 1 0 01-1 1A17 17 0 013 4a1 1 0 011-1h3.5a1 1 0 011 1c0 1.25.2 2.45.57 3.57a1 1 0 01-.25 1z"/></svg>555.310.4127</li>
        <li class="contact__item"><svg class="icon" viewBox="0 0 24 24"><path d="M6 2h12v6H6zM3 9h18v9h-3v4H6v-4H3zM8 15v5h8v-5z"/></svg>555.310.4128</li>
        <li class="contact__item"><svg class="icon" viewBox="0 0 24 24"><path d="M2 5h20v14H2zm2 2v.4l8 5 8-5V7z"/></svg>info@pinecrestlockworks.com</li>
        <li class="contact__item"><svg class="icon" viewBox="0 0 24 24"><circle cx="12" cy="12" r="10"/></svg>www.pinecrestlockworks.com</li>
      </ul>
    </div>
    <p class="address"><svg class="icon" viewBox="0 0 24 32"><path d="M12 0a12 12 0 00-12 12c0 9 12 20 12 20s12-11 12-20A12 12 0 0012 0zm0 17a5 5 0 110-10 5 5 0 010 10z"/></svg>48 Alder Ridge Road, Brookfield, ON L5T 3K2</p>
  </section>

  <section class="card card--back">
    <div class="brand">
      <span class="brand__mark"></span>
      <span class="brand__name">Pinecrest Lockworks</span>
    </div>
  </section>
</body>
</html>
```